Header/Banner Design for Website

Looking for a banner/header design for www.fixerupperdiaries.net Should be fun and whimsical, and include the name of the website, something to do with home improvement or tools, and a caricature of a young, beautiful 20 something blond who the website revolves around. The website is about a young woman who bought her first house and it taking on all of the renovations and remodeling on her own for the first time.

The header/banner should include the same colors that are in the website. The width should be no more than 430 pixels, the height is flexible but the current space in the header is 85 pixels...looking for some creativity. any questions, please ask. Attached an image that she liked for the image of the woman (would like to see versions of this included)
Updates

Target Market(s)

women 20+ that are new home owners or that are tackling home improvement on their own

Industry/Entity Type

Home Improvement

Requirements
Must have
• color coordinate with the website
should feature a young, blond, female caricature
should include the name of the website

```html
<!DOCTYPE html>
<html lang="en">
<head>
<meta charset="utf-8">
<title>Solo Renovation Chronicle – Header</title>
<link rel="stylesheet" href="https://fonts.googleapis.com/css2?family=Archivo:wdth,wght@125,900&display=swap">
<style>
  :root {
    --bg-pink: #d9a9c2;
    --bg-mauve: #c997b1;
    --band-pink: #f3d3e2;
    --band-line: #ffffff;
    --plum: #6b1747;
    --magenta: #d62f80;
    --ink: #3a0f27;
    --texture-grey: #b48aa0;
    --hero-pink: #e96fb0;
    --hero-blond: #f2d77a;
  }
  html, body {
    margin: 0;
    padding: 0;
    width: 1200px;
    height: 237px;
    overflow: hidden;
    background: var(--bg-pink);
  }
  .banner {
    display: block;
    width: 1200px;
    height: 237px;
  }
  .title {
    font-family: "Archivo", "Arial Black", sans-serif;
    font-weight: 900;
    font-stretch: 125%;
  }
  .title-solo { fill: var(--plum); }
  .title-renovation { fill: var(--magenta); }
  .title-chronicle { fill: var(--ink); }
</style>
</head>
<body>
<svg class="banner" viewBox="0 0 1200 237" xmlns="http://www.w3.org/2000/svg">
  <defs>
    <linearGradient id="bg-fade" x1="0" x2="1" y1="0" y2="0">
      <stop offset="0" stop-color="var(--bg-mauve)"/>
      <stop offset="0.45" stop-color="var(--bg-pink)"/>
      <stop offset="1" stop-color="#e6c2d4"/>
    </linearGradient>
    <linearGradient id="texture-fade" x1="0" x2="1" y1="0" y2="0">
      <stop offset="0" stop-color="var(--texture-grey)" stop-opacity="0"/>
      <stop offset="0.4" stop-color="var(--texture-grey)" stop-opacity="0.35"/>
      <stop offset="1" stop-color="var(--texture-grey)" stop-opacity="0.5"/>
    </linearGradient>
    <linearGradient id="hero-fill" x1="0" x2="0" y1="0" y2="1">
      <stop offset="0" stop-color="var(--hero-blond)"/>
      <stop offset="0.45" stop-color="#f0c9a8"/>
      <stop offset="1" stop-color="var(--hero-pink)"/>
    </linearGradient>
    <filter id="title-shadow" x="-5%" y="-20%" width="110%" height="150%">
      <feDropShadow dx="3" dy="4" stdDeviation="2.5" flood-color="#2a0a1b" flood-opacity="0.55"/>
    </filter>
  </defs>

  <rect class="backdrop" width="1200" height="237" fill="url(#bg-fade)"/>

  <rect class="texture-area" x="560" y="0" width="640" height="237" fill="url(#texture-fade)"
        role="img" aria-label="Cracked plaster wall texture"/>

  <rect class="ornament-area" x="165" y="6" width="240" height="180" rx="50" fill="var(--texture-grey)" opacity="0.3"
        role="img" aria-label="Grey butterflies around an ornate oval frame"/>

  <g class="stripe-band">
    <rect x="0" y="139" width="1200" height="31" fill="var(--band-pink)"/>
    <line x1="0" y1="140" x2="1200" y2="140" stroke="var(--band-line)" stroke-width="2"/>
    <line x1="0" y1="169" x2="1200" y2="169" stroke="var(--band-line)" stroke-width="2"/>
  </g>

  <g class="title" filter="url(#title-shadow)">
    <text class="title-solo" x="165" y="128" font-size="90" textLength="219" lengthAdjust="spacingAndGlyphs">SOLO</text>
    <text class="title-renovation" x="474" y="128" font-size="90" textLength="681" lengthAdjust="spacingAndGlyphs">RENOVATION</text>
    <text class="title-chronicle" x="491" y="209" font-size="104" textLength="678" lengthAdjust="spacingAndGlyphs">CHRONICLE</text>
  </g>

  <rect class="hero-figure" x="6" y="6" width="150" height="231" rx="30" fill="url(#hero-fill)"
        role="img" aria-label="Cartoon of a young blond woman in a pink top holding a hammer"/>
</svg>
</body>
</html>
```